R&T Marketing / P.L.B. Sales Business Cards

I have 2 companies that are somewhat connected, yet sell to 2 different markets.

R&T Marketing www.ratendpx.example

We are a manufacturers representative company. We handle sales and marketing of Home Theater, Home Automation, Audio & Video products for the state of Florida. We work with Designers, Architects, Technology Consultants and Electronic Integrators to design, sell and install cutting edge technology in new and existing homes, condos and commercial spaces.

P.L.B. Sales www.plbpx.example

We are a manufacturers representative company. We handle sales and marketing of automotive Audio, Electronics, Security, Navigation and Entertainment products for the state of Florida. We work with 12-volt retailers, installers and automobile customizers to design, sell, merchandise, fabricate and install cutting edge technology in cars, boats, motor coaches, etc.

We have logo's that might still be relevant, but might need a little touching up. We need a new business card design and layout for each of the 2 companies. I would like them to have a family look, but still better speak to the customer base associated with the channel.

Target Market(s)

R&T Marketing -

Design, Engineering, Construction, Technology, elegant, tasteful.

P.L.B. Sales -

More cutting edge, industrial, youth, aggressive, fun, bold.

Requirements
Must have
• New business card layout for both companies.
Nice to have
• A family look, or relationship to the other company. Even if it's just a logo referencing the other company.

```html
<!DOCTYPE html>
<html lang="en">
<head>
<meta charset="utf-8">
<title>R&amp;T Marketing / P.L.B. Sales Business Cards</title>
<link rel="stylesheet" href="https://fonts.googleapis.com/css2?family=Arimo:wght@400;700&display=swap">
<style>
  :root {
    --backdrop: #474545;
    --sales-yellow: #fff200;
    --marketing-blue: #0095e0;
    --card-white: #ffffff;
    --ink: #111111;
    --card-edge: #2a2a2a;
  }
  * { margin: 0; padding: 0; box-sizing: border-box; }
  html, body {
    width: 1200px;
    height: 1000px;
    overflow: hidden;
    background: var(--backdrop);
    font-family: "Arimo", Arial, sans-serif;
    color: var(--ink);
  }
  .card-sheet {
    position: relative;
    width: 1200px;
    height: 1000px;
    display: flex;
    justify-content: center;
    align-items: center;
    gap: 40px;
  }
  .business-card {
    position: relative;
    width: 540px;
    height: 310px;
    background: var(--card-white);
    border: 2px solid var(--card-edge);
    box-shadow: 0 4px 14px rgba(0,0,0,0.35);
    overflow: hidden;
  }
  .brand-band {
    position: absolute;
    left: 0; top: 0;
    width: 100%;
    height: 155px;
  }
  .business-card--sales .brand-band { background: var(--sales-yellow); }
  .business-card--marketing .brand-band { background: var(--marketing-blue); }

  .brand-name {
    position: absolute;
    left: 34px;
    top: 40px;
    font-weight: 700;
    color: var(--ink);
    line-height: 0.95;
  }
  .business-card--sales .brand-name { font-size: 44px; letter-spacing: 1px; }
  .business-card--marketing .brand-name { font-size: 40px; letter-spacing: 0.5px; }

  .holder {
    position: absolute;
    right: 12px;
    top: 105px;
    text-align: right;
    font-weight: 700;
    font-size: 15px;
    letter-spacing: 1.4px;
    line-height: 21px;
    text-transform: uppercase;
  }
  .contact-block {
    position: absolute;
    right: 12px;
    top: 172px;
    text-align: right;
    font-size: 13.5px;
    line-height: 19.5px;
    font-style: normal;
  }
  .sister-brands {
    position: absolute;
    left: 40px;
    bottom: 14px;
    display: flex;
    align-items: flex-end;
    gap: 30px;
  }
  .sister-brand {
    font-weight: 700;
    font-size: 13px;
    line-height: 1.05;
    color: var(--ink);
    text-transform: uppercase;
  }
</style>
</head>
<body>
<main class="card-sheet">

  <article class="business-card business-card--sales">
    <div class="brand-band">
      <div class="brand-name">P.L.B.<br>SALES</div>
      <div class="holder">Dana Whitfield<br>Rep Principle</div>
    </div>
    <address class="contact-block">
      4210 NW 19th Street<br>
      Coral Bay, FL 33000<br>
      T: 800-555-0142<br>
      F: 305-555-0187<br>
      dana@plb-rt.example<br>
      www.plb-rt.example
    </address>
    <div class="sister-brands">
      <div class="sister-brand">R&amp;T<br>Marketing</div>
      <div class="sister-brand">DDAD<br>Distributing</div>
    </div>
  </article>

  <article class="business-card business-card--marketing">
    <div class="brand-band">
      <div class="brand-name">R&amp;T<br>MARKETING</div>
      <div class="holder">Owen Kessler<br>Rep Principle</div>
    </div>
    <address class="contact-block" style="top:164px">
      4210 NW 19th Street<br>
      Coral Bay, FL 33000<br>
      T: 800-555-0142<br>
      M: 727-555-0163<br>
      F: 305-555-0187<br>
      owen@plb-rt.example<br>
      www.plb-rt.example
    </address>
    <div class="sister-brands">
      <div class="sister-brand">P.L.B.<br>Sales</div>
      <div class="sister-brand">DDAD<br>Distributing</div>
    </div>
  </article>

</main>
</body>
</html>
```